Vantrel Web Services

This is a new It services company operating in Perth western Australia

we need a website that is easy to navigate without a cluttered feel to it it should have the following links and pages

About Us
Services
Clients
Contact Us
MY Vantrel (login for clients)

Hi it is a web based IT services company so we would expect customers to come to the website for 2 different purposes the first is to enquire about our services and then as they become customers come to our website to manage their services so whilst they are seperate we want do not want it to look like 2 different websites

hope this helps

Hi to update this we need a home page and templates for sub pages

this is a design brief only and not the coding of the pages or building of the site

```html
<!DOCTYPE html>
<html lang="en">
<head>
<meta charset="utf-8">
<title>Vantrel Web Services</title>
<link rel="stylesheet" href="https://fonts.googleapis.com/css2?family=Tinos&display=swap">
<style>
  :root {
    --ink: #111111;
    --rule: #ffffff;
    --deep-red: #a8060a;
    --red: #d2262a;
    --coral: #e86a5e;
    --orange: #ee6a1c;
  }
  html, body {
    margin: 0;
    padding: 0;
    width: 1200px;
    height: 675px;
    overflow: hidden;
  }
  body {
    position: relative;
    font-family: "Tinos", "Times New Roman", serif;
    color: var(--ink);
  }
  .backdrop {
    position: absolute;
    inset: 0;
    background:
      radial-gradient(ellipse 420px 110px at 560px 120px, rgba(240,190,180,0.75), transparent 70%),
      radial-gradient(ellipse 500px 140px at 620px 560px, rgba(255,80,60,0.55), transparent 70%),
      radial-gradient(ellipse 260px 380px at 1150px 560px, rgba(40,0,0,0.7), transparent 70%),
      radial-gradient(ellipse 200px 300px at 60px 620px, rgba(60,0,0,0.55), transparent 70%),
      linear-gradient(100deg, var(--deep-red) 0%, var(--red) 25%, var(--coral) 50%, var(--orange) 78%, #f07a10 100%);
  }
  .page {
    position: absolute;
    left: 199px;
    top: 0;
    width: 802px;
    height: 675px;
    border-left: 1px solid var(--rule);
    border-right: 1px solid var(--rule);
    box-sizing: border-box;
    background: rgba(90, 20, 20, 0.08);
  }
  .sidebar {
    position: absolute;
    left: 0;
    top: 0;
    width: 134px;
    height: 461px;
    border-right: 1px solid var(--rule);
    box-sizing: border-box;
  }
  .nav-item {
    position: absolute;
    left: 10px;
    width: 116px;
    border-top: 4px solid var(--rule);
    border-bottom: 4px solid var(--rule);
    box-sizing: border-box;
    text-align: center;
    font-size: 24px;
    line-height: 30px;
    text-decoration: none;
    color: var(--ink);
  }
  .nav-single { height: 49px; padding-top: 7px; }
  .nav-double { height: 70px; padding-top: 2px; }
  .nav-about { top: 35px; }
  .nav-services { top: 108px; }
  .nav-clients { top: 181px; }
  .nav-contact { top: 254px; }
  .nav-account { top: 348px; }
  .rule {
    position: absolute;
    height: 4px;
    background: var(--rule);
  }
  .content-title {
    position: absolute;
    left: 177px;
    width: 444px;
    margin: 0;
    text-align: center;
    font-weight: normal;
    font-size: 34px;
    line-height: 34px;
  }
  .content-a { top: 15px; }
  .content-b { top: 228px; }
  .content-text {
    position: absolute;
    left: 177px;
    width: 444px;
    margin: 0;
    text-align: center;
    font-size: 16px;
    line-height: 21px;
  }
  .intro { top: 63px; }
  .intro-note { top: 150px; }
  .services-text { top: 276px; }
  .content-rule { left: 177px; width: 444px; }
  .banner-rule { left: 668px; width: 133px; }
  .banner-label {
    position: absolute;
    left: 668px;
    width: 133px;
    top: 123px;
    text-align: center;
    font-size: 16px;
  }
  .banner-text {
    position: absolute;
    left: 676px;
    width: 117px;
    margin: 0;
    text-align: center;
    font-size: 16px;
    line-height: 21px;
  }
  .banner-name { top: 170px; font-size: 20px; line-height: 26px; }
  .banner-tagline { top: 260px; }
  .footer {
    position: absolute;
    left: 0;
    top: 461px;
    width: 100%;
    height: 214px;
    border-top: 1px solid var(--rule);
    box-sizing: border-box;
    text-align: center;
    font-size: 16px;
    padding-top: 3px;
  }
  .footer-brand { margin: 24px 0 8px; }
  .footer-links { margin: 0; }
  .footer-links a { color: var(--ink); text-decoration: none; margin: 0 10px; }
  .footer-note { margin: 8px 0 0; }
</style>
</head>
<body>
  <div class="backdrop" role="img" aria-label="Abstract background of flowing red and orange light streaks"></div>
  <div class="page">
    <nav class="sidebar">
      <a class="nav-item nav-single nav-about" href="#">ABOUT US</a>
      <a class="nav-item nav-single nav-services" href="#">SERVICES</a>
      <a class="nav-item nav-single nav-clients" href="#">CLIENTS</a>
      <a class="nav-item nav-double nav-contact" href="#">CONTACT<br>US</a>
      <a class="nav-item nav-double nav-account" href="#">MY<br>VANTREL</a>
    </nav>

    <h1 class="content-title content-a">WELCOME</h1>
    <p class="content-text intro">Web based IT services for businesses across Perth, Western Australia.</p>
    <div class="rule content-rule" style="top:139px"></div>
    <p class="content-text intro-note">Existing clients can manage their services in MY Vantrel.</p>
    <div class="rule content-rule" style="top:186px"></div>

    <h2 class="content-title content-b">SERVICES</h2>
    <p class="content-text services-text">Hosting, email, support and network care,<br>set up and managed for you, all in one place.</p>
    <div class="rule content-rule" style="top:352px"></div>

    <div class="rule banner-rule" style="top:91px"></div>
    <div class="rule banner-rule" style="top:116px"></div>
    <div class="banner-label">BANNER</div>
    <p class="banner-text banner-name">Vantrel Web Services</p>
    <p class="banner-text banner-tagline">IT services made simple, from enquiry to account.</p>
    <div class="rule banner-rule" style="top:410px"></div>

    <footer class="footer">
      FOOTER
      <p class="footer-brand">Vantrel Web Services</p>
      <p class="footer-links">
        <a href="#">About Us</a><a href="#">Services</a><a href="#">Clients</a><a href="#">Contact Us</a><a href="#">MY Vantrel</a>
      </p>
      <p class="footer-note">Perth, Western Australia</p>
    </footer>
  </div>
</body>
</html>
```